Brindle Tides Boat Business Website

I would like a website that looks fresh, fun and exciting with great colors and photos of people having fun sailing and power boating. Current web page is www.brindletides.example. I want to be able to change content and photos myself once completed. Also needs to have customized info request forms and access to enrollment forms. Should work across all browsers and platforms including iPad and Mac. I have three product lines...instruction, charters and trips. See also keelhour.example/new-york, and facebook.com/brindletides, /keelhournewyork and /conchlagoonbar.
Updates

Reason: We are reviewing the designs submitted and will provide feedback asap. Thank you.

Industry/Entity Type

Business

Requirements
Must have
• self management/content management
form submissions
color, fun, excitement
links pages
photo pages
Nice to have
• calendar/class scheduling
guest book
visitor uploadable photos

```html
<!DOCTYPE html>
<html lang="en">
<head>
<meta charset="utf-8">
<title>Brindle Tides Charter Co. &amp; Nautical School</title>
<link rel="stylesheet" href="https://fonts.googleapis.com/css2?family=Roboto+Condensed:wght@700&family=Open+Sans:wght@400&display=swap">
<style>
:root{
  --navy:#0a1f7a;
  --deep:#0b3fb0;
  --mid:#1a6fd6;
  --sky:#4fb8f2;
  --pale:#9fdcfb;
  --ink:#0b2466;
  --copy:#1b2f7a;
  --white:#ffffff;
  --orange:#f7a21b;
  --footer:#02082e;
  --footer-text:#6f82b4;
  --footer-dim:#2e3d6e;
  --teal:#1d9aa0;
}
*{margin:0;padding:0;box-sizing:border-box}
html,body{width:1200px;height:1147px;overflow:hidden}
body{position:relative;font-family:"Open Sans",Verdana,sans-serif;color:var(--ink);background:var(--deep)}
.abs{position:absolute}
.scenery{left:0;top:0;width:1200px;height:990px;background:
  radial-gradient(ellipse 90px 120px at 60px 170px,rgba(255,255,255,.75),rgba(255,255,255,0)),
  radial-gradient(ellipse 90px 120px at 1150px 160px,rgba(255,255,255,.75),rgba(255,255,255,0)),
  linear-gradient(180deg,#3d8fe0 0%,#6fc0f0 14%,#a9def8 30%,#59b4ee 34%,#2a86e0 48%,#1256c8 70%,#0b3fb0 100%)}
.topbar{left:0;top:0;width:1200px;height:33px;background:linear-gradient(180deg,#1240b0,#0a2a8a)}
.nav{left:0;top:0;height:33px;width:1200px;list-style:none}
.nav li{position:absolute;top:0;height:33px;line-height:33px;font-family:"Roboto Condensed",Arial,sans-serif;font-weight:700;font-size:11.5px;color:var(--white);transform:translateX(-50%);white-space:nowrap}
.nav li.active{background:var(--navy);height:45px;width:62px;text-align:center;clip-path:polygon(0 0,100% 0,100% 100%,50% 88%,0 100%)}
.logo{left:146px;top:0;width:264px;height:104px;background:var(--white);box-shadow:0 2px 6px rgba(0,0,0,.3);display:flex;align-items:center;justify-content:center;gap:8px}
.logo-dot{width:14px;height:14px;border-radius:50%;background:var(--orange)}
.logo-name{font-family:"Open Sans",sans-serif;font-size:26px;color:var(--teal)}
.hero{left:121px;top:31px;width:961px;height:318px;border:2px solid var(--deep);background:
  linear-gradient(115deg,rgba(255,255,255,0) 38%,rgba(255,255,255,.85) 48%,rgba(240,243,246,.9) 60%,rgba(255,255,255,0) 72%),
  linear-gradient(180deg,#9fb3c8 0%,#c4d2df 40%,#d9e2ea 72%,#4f7fae 76%,#36628f 80%,#8a929b 84%,#5a636d 100%)}
.call{left:791px;top:249px;width:281px;height:36px;background:var(--navy);color:var(--white);font-family:"Roboto Condensed",Arial,sans-serif;font-weight:700;font-size:21px;line-height:36px;padding-left:13px;white-space:nowrap}
.call span{color:var(--orange)}
.mail{left:791px;top:285px;width:281px;height:36px;background:linear-gradient(180deg,#37a8f0,#1d86e0);color:var(--white);font-family:"Roboto Condensed",Arial,sans-serif;font-weight:700;font-size:16px;line-height:36px;text-align:center;white-space:nowrap}
.strip{left:119px;top:353px;width:964px;height:124px;background:linear-gradient(180deg,#0b3fb0 0%,#1a6fd6 70%,var(--pale) 72%,var(--pale) 100%)}
.card{top:362px;width:117px;height:106px;border:2px solid var(--navy);background:var(--navy)}
.card h3{height:15px;line-height:15px;font-family:Arial,sans-serif;font-size:9.5px;font-weight:700;color:var(--white);text-align:center;background:linear-gradient(180deg,#2a55c0,#0a1f7a);border-radius:4px 4px 0 0;white-space:nowrap}
.card .photo{height:87px}
.panel{left:119px;top:477px;width:964px;height:497px;background:var(--white)}
.welcome{left:152px;top:510px;font-size:27px;font-weight:400;color:var(--ink)}
.copy{left:154px;top:562px;width:572px;font-size:11.6px;line-height:13px;letter-spacing:.25px;color:var(--copy)}
.copy p{margin-bottom:13px}
.feature{left:806px;top:527px;width:258px;height:222px;background:
  linear-gradient(170deg,rgba(255,255,255,0) 45%,rgba(255,255,255,.9) 46%,rgba(255,255,255,.9) 48%,rgba(255,255,255,0) 49%),
  linear-gradient(180deg,#6f93b8 0%,#9fbfd8 45%,#4d7ea8 62%,#7fb0d8 100%);box-shadow:0 2px 6px rgba(0,0,0,.3)}
.seal{left:956px;top:508px;width:104px;height:104px;border-radius:50%;background:radial-gradient(circle,#f7c531 0%,#e39a12 100%)}
.sec{top:793px;font-size:18px;font-weight:400;color:var(--ink)}
.box{top:830px;width:301px;height:129px;background:linear-gradient(180deg,#1a8ee8,#0b4fc0)}
.thumb{width:71px;height:54px;border:1px solid #cfe6f8}
.lbl{font-size:12px;color:#d7ecff;text-align:right;width:80px}
.field{width:195px;height:24px;border-radius:12px;background:var(--white);border:2px solid #5c6f94}
.book{left:649px;top:919px;width:89px;height:29px;border-radius:9px;background:linear-gradient(180deg,#ffb627,#f07c0b);color:var(--white);font-family:"Roboto Condensed",Arial,sans-serif;font-weight:700;font-size:13px;line-height:29px;text-align:center}
.quote{left:806px;top:852px;width:222px;font-size:11.5px;line-height:13px;color:var(--white)}
.qmark{font-size:18px;color:#9fd0f8;font-family:Georgia,serif}
.author{left:850px;top:916px;width:190px;text-align:right;font-size:11.5px;color:#b9dcfa}
.band{left:0;top:974px;width:1200px;height:16px;background:var(--deep)}
.footer{left:0;top:990px;width:1200px;height:157px;background:var(--footer)}
.fnav li{position:absolute;top:1016px;list-style:none;font-family:"Roboto Condensed",Arial,sans-serif;font-weight:700;font-size:11.5px;color:var(--footer-text);transform:translateX(-50%);white-space:nowrap}
.fcontact{left:0;top:1060px;width:1143px;text-align:center;font-family:"Roboto Condensed",Arial,sans-serif;font-weight:700;font-size:11.5px;color:var(--footer-dim)}
.social{top:1091px;width:23px;height:23px;border-radius:3px}
</style>
</head>
<body>
<div class="abs scenery" role="img" aria-label="Blue sky with clouds and seagulls above a sparkling open sea"></div>
<div class="abs topbar"></div>

<div class="abs hero" role="img" aria-label="Sailor at the helm of a large white sailing yacht on open water"></div>
<div class="abs call">CALL US NOW : <span>555-014-4600</span></div>
<div class="abs mail">EMAIL: INFO@BRINDLETIDES.EXAMPLE</div>

<div class="abs logo"><span class="logo-dot"></span><span class="logo-name">Brindle Tides</span></div>

<ul class="abs nav">
  <li class="active" style="left:530px">HOME</li>
  <li style="left:628px">CHARTER SAILING</li>
  <li style="left:749px">NAUTICAL SCHOOL</li>
  <li style="left:869px">CHARTER POWER</li>
  <li style="left:966px">TRAVEL</li>
  <li style="left:1041px">CONTACT</li>
</ul>

<div class="abs strip"></div>
<div class="abs card" style="left:130px"><h3>Nautical Courses</h3><div class="photo" role="img" aria-label="Catamaran sailing" style="background:linear-gradient(180deg,#b9d0e6 0%,#9fbcd8 60%,#3f6f9e 62%,#4c7fae 100%)"></div></div>
<div class="abs card" style="left:263px"><h3>Charter Sailing</h3><div class="photo" role="img" aria-label="Fishing reel over boat wake" style="background:linear-gradient(180deg,#8fd0f4 0%,#3f9be0 40%,#e6f4fb 75%,#2a7fd0 100%)"></div></div>
<div class="abs card" style="left:401px"><h3>Diving &amp; Certication</h3><div class="photo" role="img" aria-label="Scuba diver underwater" style="background:radial-gradient(circle at 60% 50%,#6a7be8,#2a3ac0 60%,#1c2a9a)"></div></div>
<div class="abs card" style="left:542px"><h3>Beach Outings</h3><div class="photo" role="img" aria-label="White sand beach with dune grass" style="background:linear-gradient(180deg,#3aa6e8 0%,#9fd8f4 45%,#e9f0ea 60%,#f3f1ea 100%)"></div></div>
<div class="abs card" style="left:682px"><h3>Adventure Travel</h3><div class="photo" role="img" aria-label="Anglers holding their catch" style="background:linear-gradient(180deg,#b8d2ea 0%,#8fa9c2 45%,#6e7f90 75%,#4f5c6a 100%)"></div></div>
<div class="abs card" style="left:822px"><h3>Lunch by the Sea</h3><div class="photo" role="img" aria-label="Seafood lunch by turquoise water" style="background:linear-gradient(90deg,#2fc4c9 0%,#1fa6bb 60%,#d8cbb8 80%,#3a3a3a 100%)"></div></div>
<div class="abs card" style="left:958px"><h3>Hire Captain</h3><div class="photo" role="img" aria-label="Captain and guest with a fish on deck" style="background:linear-gradient(180deg,#a6c4de 0%,#8aa8c0 40%,#a08468 70%,#6b6552 100%)"></div></div>

<div class="abs panel"></div>
<h1 class="abs welcome">Welcome</h1>
<div class="abs copy">
  <p>Few, if any, locations in Manhattan offer you a wider range of boating options than Brindle Tides Charter Co. and Nautical School.&nbsp; If you're interested in boating on New York's 'Sixth Borough', whether your a sailor or power boater, scallywag or seasoned salt, chances are we've got some-thing you're looking for.</p>
  <p>We operate KeelHour New York (www.keelhour.example/new-york) the world's largest fractional boating company with bases in the US, Europe and Australia offering seasonal memberships on sail and power boats from 25' through 50'.&nbsp; We take the hassle and cost out of boating by providing access to a professionally maintained fleet that you can schedule through an on-line calendar.&nbsp; All you have to do is show up and go!</p>
  <p>Brindle Tides Charter Co. gives you access to a fleet of power and sail vessels to explore the Hudson, New York Harbor, the East River and Long Island Sound for a day, a weekend or a week. Our "Captained Cruises" put an experienced sailor in charge of the ship; you can steer the boat,</p>
</div>
<div class="abs feature" role="img" aria-label="Sailboat and crew in life jackets sailing on a sunny bay"></div>
<div class="abs seal" role="img" aria-label="Satisfaction guarantee seal"></div>

<h2 class="abs sec" style="left:142px">Users gallery</h2>
<h2 class="abs sec" style="left:457px">Newsletter sign up</h2>
<h2 class="abs sec" style="left:770px">Testimonials</h2>

<div class="abs box" style="left:137px"></div>
<div class="abs thumb" style="left:154px;top:836px;background:linear-gradient(180deg,#9fc8ea 0%,#7fb6e0 40%,#8a7a6a 75%,#5d7086 100%)" role="img" aria-label="Angler with fish"></div>
<div class="abs thumb" style="left:247px;top:836px;background:linear-gradient(180deg,#c6e0f4 0%,#9fc6e6 50%,#5a7fa8 75%,#4a6c96 100%)" role="img" aria-label="Group on a boat deck"></div>
<div class="abs thumb" style="left:337px;top:836px;background:linear-gradient(180deg,#8fbde4 0%,#6fa4d4 40%,#a8866e 70%,#8a6f5e 100%)" role="img" aria-label="Crew showing their catch"></div>
<div class="abs thumb" style="left:154px;top:898px;background:radial-gradient(ellipse at 50% 50%,#cfe9fb,#3aa0e8 45%,#1a62c0)" role="img" aria-label="Shark swimming underwater"></div>
<div class="abs thumb" style="left:247px;top:898px;background:linear-gradient(180deg,#b6d6ef 0%,#9ec8ea 35%,#9c8670 65%,#7d6a58 100%)" role="img" aria-label="Fishing group lined up with fish"></div>
<div class="abs thumb" style="left:337px;top:898px;background:linear-gradient(180deg,#bfdcf2 0%,#a3cdee 45%,#e8eef2 60%,#2f6fae 100%)" role="img" aria-label="Motor boat at sea"></div>

<div class="abs box" style="left:451px"></div>
<div class="abs lbl" style="left:452px;top:850px">Your Name</div>
<div class="abs field" style="left:544px;top:848px"></div>
<div class="abs lbl" style="left:452px;top:888px">Phone No</div>
<div class="abs field" style="left:544px;top:885px"></div>
<div class="abs book">BOOK NOW</div>

<div class="abs box" style="left:766px"></div>
<div class="abs qmark" style="left:789px;top:838px">&ldquo;</div>
<p class="abs quote">Lorem Ipsum has been the industry's standard dummy text ever since the 1500s, when an unknown printer took</p>
<div class="abs qmark" style="left:1027px;top:883px">&rdquo;</div>
<div class="abs author">Miles Garrow Tampa FLORIDA</div>

<div class="abs band"></div>
<div class="abs footer"></div>
<ul class="fnav">
  <li style="left:217px">HOME</li>
  <li style="left:349px">CHARTER SAILING</li>
  <li style="left:509px">NAUTICAL SCHOOL</li>
  <li style="left:666px">CHARTER POWER</li>
  <li style="left:802px">TRAVEL</li>
  <li style="left:914px">CONTACT</li>
</ul>
<div class="abs fcontact">CALL US AT 555-820-SAIL (7245), OR EMAIL DESK@BRINDLETIDES.EXAMPLE.</div>
<div class="abs social" style="left:556px;background:#3b5aa0" aria-label="Social link"></div>
<div class="abs social" style="left:590px;background:#3fb6ea" aria-label="Social link"></div>
</body>
</html>
```